Automotive Parts Company Business Card/Logo Design

We need a logo/business card for a new automotive parts and accessories company which is based in Barbados. The company will only have an online presence and this will reduce our overheads and allow us to pass potential savings to our customers.

We will offer most automotive parts which include, but are not limited to, accessories, exterior, interior, body parts.

We want to appeal to a very wide audience and we're looking for a modern, clean and bold design to make the company seem very professional. Our logo and facebook page will be our only customer facing items. So it is essential that these are done correctly.

The design should really communicate that we can provide premium car parts at affordable prices for all types of cars e.g. European and Japanese.

We will stock items and also source hard to get and unique pieces. We aim to not just be another shop that sells parts. But we want to work with our customers to achieve their car goals.

The company name is GearNest and our slogan is Quality Parts At Affordable Prices.
The design should be very modern, clean and bold.

I've included examples of some of the business cards I like as well as images of car products.
Updates

Dear Designers,

I've uploaded some samples of some business card/logo designs I like. Please have a look at the project brief. Just to reiterate, I am looking for a clean, modern design.

Thanks,

Rohan

Dear Designers,

Please note the Apr 14th deadline is soon approaching.

Also note the business card is double-sided.

I look forward to working with you.

Thanks,

Rohan

Target Market(s)

20 - 30 (young professionals, younger generation with disposible income) and then then all other markets

Industry/Entity Type

Automotive

Contact Information for Business Card

Rohan Mehtabrooke
GearNest
Quality Parts At Affordable Prices
https://www.example-social.test/gearnestbb
246-555-0192
gearnestbb@mailbox-demo.test

```html
<!DOCTYPE html>
<html lang="en">
<head>
<meta charset="utf-8">
<title>GearNest Business Card</title>
<link href="https://fonts.googleapis.com/css2?family=Michroma&family=Montserrat:wght@400;600&display=swap" rel="stylesheet">
<style>
  :root {
    --canvas: #e9e7e4;
    --card-dark: #231f20;
    --blue: #2f8fbf;
    --blue-deep: #1b6fa6;
    --blue-light: #3aa0c9;
    --silver: #c9cdd2;
    --white: #ffffff;
    --pattern-1: #2f2b2c;
    --pattern-2: #242021;
  }
  * { box-sizing: border-box; margin: 0; padding: 0; }
  html, body {
    width: 1200px; height: 1000px; overflow: hidden;
    background: var(--canvas);
  }
  .canvas { position: relative; width: 1200px; height: 1000px; }
  .card {
    position: absolute; left: 190px; width: 820px; height: 440px;
    border-radius: 34px; overflow: hidden;
    background: var(--card-dark);
    box-shadow: 0 8px 24px rgba(0,0,0,0.18);
  }
  .card--front { top: 50px; }
  .card--back { top: 520px; }
  .card__pattern {
    position: absolute; inset: 0;
    background: radial-gradient(ellipse at 55% 45%, var(--pattern-1) 0%, var(--pattern-2) 55%, var(--card-dark) 100%);
  }
  .card__band {
    position: absolute; left: 0; right: 0; bottom: 0;
    background: linear-gradient(90deg, var(--blue-deep), var(--blue-light));
  }
  .card__band::before {
    content: ""; position: absolute; left: 0; right: 0; top: -6px; height: 6px;
    background: linear-gradient(90deg, #555 0%, var(--silver) 50%, #555 100%);
  }
  .card--front .card__band { height: 92px; }
  .card--back .card__band { height: 250px; }

  .brand-name {
    position: absolute; left: 0; right: 0; text-align: center;
    font-family: "Montserrat", sans-serif; font-weight: 600;
    color: var(--white); letter-spacing: 1px; line-height: 1;
  }
  .brand-tagline {
    position: absolute; left: 0; right: 0; text-align: center;
    font-family: "Michroma", sans-serif; text-transform: uppercase;
    color: var(--white); letter-spacing: 2px; line-height: 1.2;
  }
  .card--front .brand-name { top: 128px; font-size: 80px; }
  .card--front .brand-tagline { top: 238px; font-size: 19px; }
  .website {
    position: absolute; left: 0; right: 0; bottom: 28px; text-align: center;
    font-family: "Montserrat", sans-serif; font-size: 24px; color: var(--white);
  }

  .card--back .brand-name { top: 52px; font-size: 62px; }
  .card--back .brand-tagline { top: 138px; font-size: 20px; }
  .contact {
    position: absolute; left: 0; right: 0; bottom: 0; height: 250px;
    display: flex; flex-direction: column; align-items: center; padding-top: 30px;
    font-family: "Montserrat", sans-serif; color: var(--white);
  }
  .contact__name { font-size: 34px; font-weight: 600; margin-bottom: 18px; }
  .contact__line {
    display: flex; align-items: center; gap: 8px;
    font-size: 24px; font-weight: 400; line-height: 36px;
  }
  .contact__icon { width: 20px; height: 20px; flex: none; }
</style>
</head>
<body>
<div class="canvas">

  <section class="card card--front">
    <div class="card__pattern" role="img" aria-label="Faint dark pattern of car parts: wheels, tyres and brake discs"></div>
    <h1 class="brand-name">GearNest</h1>
    <p class="brand-tagline">Quality Parts At Affordable Prices</p>
    <div class="card__band"></div>
    <p class="website">www.gearnest-parts.test</p>
  </section>

  <section class="card card--back">
    <div class="card__pattern" role="img" aria-label="Faint dark pattern of car parts: wheels, tyres and brake discs"></div>
    <h2 class="brand-name">GearNest</h2>
    <p class="brand-tagline">Parts At Affordable Prices</p>
    <div class="card__band"></div>
    <div class="contact">
      <p class="contact__name">Rohan Mehtabrooke</p>
      <p class="contact__line">
        <svg class="contact__icon" viewBox="0 0 20 20" aria-hidden="true"><rect x="5" y="1.5" width="10" height="17" rx="2" fill="none" stroke="#fff" stroke-width="1.6"/><circle cx="10" cy="15.5" r="1" fill="#fff"/></svg>
        246-555-0192
      </p>
      <p class="contact__line">
        <svg class="contact__icon" viewBox="0 0 20 20" aria-hidden="true"><rect x="1.5" y="4" width="17" height="12" fill="none" stroke="#fff" stroke-width="1.6"/><path d="M1.5 4 L10 11 L18.5 4" fill="none" stroke="#fff" stroke-width="1.6"/></svg>
        gearnestbb@mailbox-demo.test
      </p>
      <p class="contact__line">
        <svg class="contact__icon" viewBox="0 0 20 20" aria-hidden="true"><rect x="2" y="2" width="16" height="16" rx="2" fill="#fff"/></svg>
        www.example-social.test/gearnestbb
      </p>
    </div>
  </section>

</div>
</body>
</html>
```